Business Card Design

New business card design

Target Market(s)

Residential & Commercial Property Managers

Industry/Entity Type

Plumbing Services

Contact Information for Business Card

Name - Owen Tredgold, title - Director, Phone Number - 0431 862 507, email - owen@rvb-plumbing.com.au, Company ABN - 73 215 904 386,

Font styles to use
Sans Serif

Colors
0054AA
0677BA
7BADD7
CADEEF
E8F1F8

```html
<!DOCTYPE html>
<html lang="en">
<head>
<meta charset="utf-8">
<title>RVB Plumbing Services – Business Card</title>
<link href="https://fonts.googleapis.com/css2?family=Poppins:wght@300;400;600&display=swap" rel="stylesheet">
<style>
  :root {
    --scene: #2e2e2e;
    --card: #1e2329;
    --accent: #00a9ec;
    --ink: #ffffff;
    --card-w: 640px;
    --card-h: 391px;
  }
  * { margin: 0; padding: 0; box-sizing: border-box; }
  html, body {
    width: 1200px; height: 1015px; overflow: hidden;
    background: var(--scene);
    font-family: "Poppins", sans-serif;
  }
  .sheet {
    width: 1200px; height: 1015px;
    display: flex; flex-direction: column;
    align-items: center; justify-content: center; gap: 60px;
  }
  .card {
    position: relative;
    width: var(--card-w); height: var(--card-h);
    background: var(--card);
    overflow: hidden;
    box-shadow: 0 14px 30px rgba(0,0,0,.45);
  }
  .card__band {
    position: absolute; left: 0; right: 0; bottom: 0;
    height: 8px; background: var(--accent);
  }

  /* Front */
  .brand {
    position: absolute; left: 0; right: 0; top: 110px;
    text-align: center; color: var(--ink);
  }
  .brand__name {
    display: inline-flex; align-items: center; gap: 14px;
    font-weight: 300; font-size: 110px; line-height: 1; letter-spacing: 2px;
  }
  .brand__dot {
    width: 26px; height: 26px; border-radius: 50%;
    background: var(--accent); margin-top: 40px;
  }
  .brand__tagline {
    margin-top: 22px;
    font-weight: 300; font-size: 15px; letter-spacing: 14px;
    text-transform: lowercase;
  }

  /* Back */
  .contact {
    position: absolute; left: 34px; top: 120px;
  }
  .contact__id {
    display: flex; align-items: stretch; gap: 12px;
  }
  .contact__marker {
    width: 34px; background: var(--accent);
  }
  .contact__name {
    color: var(--accent); font-weight: 600; font-size: 22px;
    line-height: 1.05; text-transform: uppercase;
  }
  .contact__role {
    color: var(--ink); font-weight: 400; font-size: 18px; line-height: 1.1;
  }
  .contact__lines {
    list-style: none; margin: 34px 0 0 58px;
    color: var(--ink); font-size: 18px; line-height: 1.3;
  }
  .contact__lines li { display: flex; align-items: center; gap: 10px; }
  .contact__lines svg { width: 18px; height: 18px; fill: var(--accent); flex: none; }
  .contact__abn {
    margin: 56px 0 0 58px; color: var(--ink); font-size: 18px;
  }
  .contact__abn span { color: var(--accent); }
  .accent-disc {
    position: absolute; right: 48px; top: 62px;
    width: 220px; height: 220px; border-radius: 50%;
    background: var(--accent);
  }
</style>
</head>
<body>
<main class="sheet">
  <section class="card card--front">
    <div class="brand">
      <div class="brand__name">rvb<span class="brand__dot"></span></div>
      <p class="brand__tagline">plumbing services</p>
    </div>
    <div class="card__band"></div>
  </section>

  <section class="card card--back">
    <div class="contact">
      <div class="contact__id">
        <div class="contact__marker"></div>
        <div>
          <p class="contact__name">Owen Tredgold</p>
          <p class="contact__role">Director</p>
        </div>
      </div>
      <ul class="contact__lines">
        <li>
          <svg viewBox="0 0 24 24" aria-hidden="true"><path d="M6.6 10.8a15.1 15.1 0 0 0 6.6 6.6l2.2-2.2c.3-.3.7-.4 1-.2 1.1.4 2.3.6 3.6.6.6 0 1 .4 1 1V20c0 .6-.4 1-1 1A17 17 0 0 1 3 4c0-.6.4-1 1-1h3.5c.6 0 1 .4 1 1 0 1.3.2 2.5.6 3.6.1.3 0 .7-.2 1z"/></svg>
          0431 862 507
        </li>
        <li>
          <svg viewBox="0 0 24 24" aria-hidden="true"><path d="M2 5h20v14H2zm2 2v.5l8 5 8-5V7zm0 2.8V17h16V9.8l-8 5z"/></svg>
          owen@rvb-plumbing.com.au
        </li>
      </ul>
      <p class="contact__abn"><span>Company ABN</span> - 73 215 904 386</p>
    </div>
    <div class="accent-disc"></div>
    <div class="card__band"></div>
  </section>
</main>
</body>
</html>
```